P&H RESTORATION

I want a brochure similiar to the example i've attached.
My company name is Northfield Renewal. The website is: northfield-renewal.example.
The phone number is 803.417.9056.

I don't like the "yellow" being the main color of the example so I'm open to suggestions. I want something CLEAN & Simple, like our logo . This will be a bi fold brochure

```html
<!DOCTYPE html>
<html lang="en">
<head>
<meta charset="utf-8">
<title>Northfield Renewal — Bi-fold Brochure</title>
<link href="https://fonts.googleapis.com/css2?family=Poppins:ital,wght@0,400;0,500;0,600;0,700;1,400;1,500&display=swap" rel="stylesheet">
<style>
  :root{
    --backdrop:#5d5d60;
    --ink:#1c1c1a;
    --paper:#f4f4f4;
    --muted:#6b6b6b;
    --white:#ffffff;
  }
  *{box-sizing:border-box;margin:0;padding:0}
  html,body{width:1200px;height:1009px;overflow:hidden;background:var(--backdrop)}
  body{position:relative;font-family:"Poppins",sans-serif;color:var(--ink)}

  .spread{position:absolute;left:260px;width:680px;height:480px;background:var(--paper);overflow:hidden;box-shadow:0 6px 18px rgba(0,0,0,.35)}
  .spread--inside{top:16px;background:linear-gradient(90deg,#fafafa 0%,#ececec 49.8%,#f7f7f7 50.2%,#e9e9e9 100%)}
  .spread--outside{top:513px}
  .abs{position:absolute}
  .fold{position:absolute;left:340px;top:0;width:1px;height:100%;background:rgba(0,0,0,.08)}

  .shape{position:absolute;inset:0}
  .photo{position:absolute;inset:0}

  .heading{font-weight:700;line-height:1.05;letter-spacing:.2px}
  .heading--lg{font-size:25px}
  .lede{font-style:italic;font-size:10.5px;line-height:1.3;color:var(--muted);text-align:justify}
  .hex-icon{position:absolute;width:66px;height:60px}
  .service-note{position:absolute;width:72px;font-size:4.6px;line-height:1.25;color:var(--muted);text-align:justify}
  .support-title{position:absolute;left:0;width:340px;top:256px;text-align:center;font-weight:600;font-size:12.5px}
  .support-text{position:absolute;left:50px;width:240px;top:274px;text-align:center;font-size:9.5px;line-height:1.25;color:var(--muted)}
  .quote-mark{position:absolute;font-weight:700;color:var(--white);line-height:1}
  .quote-text{position:absolute;color:var(--white);font-style:italic;font-weight:500}

  .step{position:absolute;width:150px}
  .step-icon{position:absolute;left:-27px;top:-2px;width:18px;height:20px}
  .step-title{font-weight:600;font-size:9.4px;line-height:1.1}
  .step-text{font-size:5.8px;line-height:1.55;color:var(--muted);margin-top:3px}
  .rule-v{position:absolute;width:1px;background:var(--ink)}
  .rule-v--light{background:var(--white);width:1.5px}
  .name-mark{position:absolute;font-weight:400;white-space:nowrap}

  .intro-note{position:absolute;left:150px;top:24px;width:152px;text-align:right;color:var(--white);font-size:8.7px;line-height:1.22}
  .contact-title{position:absolute;left:0;width:340px;top:312px;text-align:center;font-weight:700;font-size:20px}
  .contact-dash{position:absolute;left:160px;top:350px;width:20px;height:1.5px;background:var(--ink)}
  .contact-line{position:absolute;font-size:7.4px;line-height:1.75}
  .address{position:absolute;left:0;width:340px;top:407px;text-align:center;font-size:7.4px;line-height:1.35}

  .cover-title{position:absolute;left:367px;top:310px;line-height:.98}
  .cover-title .eyebrow{display:block;font-weight:500;font-size:20.5px;letter-spacing:.3px}
  .cover-title .main{display:block;font-weight:700;font-size:31px;letter-spacing:.2px}
  .cover-underline{position:absolute;left:367px;top:404px;width:70px;height:3px;background:var(--ink)}
  .cover-text{position:absolute;left:367px;top:416px;width:250px;font-size:6.7px;line-height:1.3;color:var(--muted)}
  .cover-url{position:absolute;left:367px;top:459px;font-weight:500;font-size:8.4px;display:flex;align-items:center;gap:2px;width:313px}
  .cover-url::after{content:"";flex:1;height:.8px;background:var(--ink);margin-top:3px}
  .vertical-name{position:absolute;left:400px;top:40px;transform-origin:left top;transform:rotate(90deg);color:var(--white);font-size:15px;white-space:nowrap}
</style>
</head>
<body>

<!-- Inside spread -->
<section class="spread spread--inside" aria-label="Inside spread">
  <div class="photo" role="img" aria-label="Dim photo of restoration crew at work"
       style="clip-path:polygon(0 76.5%,50% 60.6%,50% 100%,0 100%);background:linear-gradient(160deg,#2a2a28 0%,#1a1a19 55%,#2e2f2c 100%)"></div>
  <svg class="shape" width="680" height="480" viewBox="0 0 680 480" aria-hidden="true">
    <polygon points="0,288 154,327 0,361" fill="var(--ink)"/>
    <polygon points="340,441 508,367 680,367 680,480 340,480" fill="var(--ink)"/>
  </svg>
  <div class="photo" role="img" aria-label="Photo of a water-damaged room during restoration"
       style="clip-path:polygon(50% 60.4%,74.7% 76.5%,50% 91.9%);background:linear-gradient(135deg,#e9e4da 0%,#b9ac97 45%,#6e6353 100%)"></div>

  <h2 class="heading heading--lg abs" style="left:23px;top:12px">Our<br>Best Service</h2>
  <p class="lede abs" style="left:23px;top:74px;width:300px">Consectetuer adipiscing elit sed diam nonummy nibh euismod tincidunt ut laoreet dolore magna aliquam erat volutpat.</p>

  <svg class="hex-icon" style="left:42px;top:126px" viewBox="0 0 66 60" aria-hidden="true">
    <polygon points="17,2 49,2 65,30 49,58 17,58 1,30" fill="var(--white)" stroke="var(--ink)" stroke-width="1.3"/>
    <polygon points="19,5.5 47,5.5 61,30 47,54.5 19,54.5 5,30" fill="var(--ink)"/>
    <rect x="22" y="24" width="18" height="6" rx="1" fill="var(--white)"/>
    <rect x="28" y="19" width="6" height="5" fill="var(--white)"/>
    <rect x="24" y="17" width="14" height="2.5" rx="1" fill="var(--white)"/>
    <rect x="36" y="27" width="5" height="7" fill="var(--white)"/>
    <path d="M38.5 37 l-2 4 a2 2 0 0 0 4 0z" fill="var(--white)"/>
  </svg>
  <svg class="hex-icon" style="left:137px;top:126px" viewBox="0 0 66 60" aria-hidden="true">
    <polygon points="17,2 49,2 65,30 49,58 17,58 1,30" fill="var(--white)" stroke="var(--ink)" stroke-width="1.3"/>
    <polygon points="19,5.5 47,5.5 61,30 47,54.5 19,54.5 5,30" fill="var(--ink)"/>
    <path d="M20 30 L33 18 L46 30" fill="none" stroke="var(--white)" stroke-width="2.5" stroke-linejoin="round"/>
    <rect x="24" y="29" width="18" height="12" fill="var(--white)"/>
    <rect x="30" y="32" width="7" height="6" fill="var(--ink)"/>
    <line x1="33.5" y1="32" x2="33.5" y2="38" stroke="var(--white)" stroke-width="1"/>
  </svg>
  <svg class="hex-icon" style="left:232px;top:126px" viewBox="0 0 66 60" aria-hidden="true">
    <polygon points="17,2 49,2 65,30 49,58 17,58 1,30" fill="var(--white)" stroke="var(--ink)" stroke-width="1.3"/>
    <polygon points="19,5.5 47,5.5 61,30 47,54.5 19,54.5 5,30" fill="var(--ink)"/>
    <circle cx="36" cy="26" r="7" fill="none" stroke="var(--white)" stroke-width="3" stroke-dasharray="3 2"/>
    <circle cx="36" cy="26" r="2.5" fill="var(--white)"/>
    <path d="M22 40 l8 -8 l4 4 l-8 8z" fill="var(--white)"/>
  </svg>

  <p class="service-note" style="left:39px;top:197px">Contrary to popular belief, Lorem Ipsum is not simply rakm text has roots piece class Latin literature. Contrary to popular belief, Lorem Ipsum is not simply rakm text has roots</p>
  <p class="service-note" style="left:134px;top:197px">Contrary to popular belief, Lorem Ipsum is not simply rakm text has roots piece class Latin literature. Contrary to popular belief, Lorem Ipsum is not simply rakm text has roots</p>
  <p class="service-note" style="left:229px;top:197px">Contrary to popular belief, Lorem Ipsum is not simply rakm text has roots piece class Latin literature. Contrary to popular belief, Lorem Ipsum is not simply rakm text has roots</p>

  <h3 class="support-title">CUSTOMER SUPPORT</h3>
  <p class="support-text">Contrary to popular belief Lorem Ipsum is not simply random text. It has roots in piece.</p>

  <span class="quote-mark" style="left:193px;top:334px;font-size:52px;height:34px">”</span>
  <p class="quote-text" style="left:110px;width:200px;top:382px;text-align:center;font-size:13.5px;line-height:1.5">Lorem ipsum dolor thesit the amet, conse tetueri that adipiscing that elitsed .</p>

  <h2 class="heading heading--lg abs" style="left:361px;top:17px">How<br>We Work</h2>
  <p class="lede abs" style="left:361px;top:79px;width:285px;text-align:left">Lorem ipsum dolor Lorem ipsum Lorem ipsum dolor sit amet conse teter adipiscing.</p>

  <div class="rule-v" style="left:506px;top:136px;height:167px"></div>

  <div class="step" style="left:396px;top:134px">
    <svg class="step-icon" viewBox="0 0 18 20" aria-hidden="true"><polygon points="9,0 18,5 18,15 9,20 0,15 0,5" fill="var(--ink)"/><path d="M5 8h2l5-3v10l-5-3H5z" fill="var(--white)"/></svg>
    <h4 class="step-title">Creative Marketing</h4>
    <p class="step-text">Euismod tincidunt utthis laoreet<br>dolore magna aliquam</p>
  </div>
  <div class="step" style="left:396px;top:197px">
    <svg class="step-icon" viewBox="0 0 18 20" aria-hidden="true"><polygon points="9,0 18,5 18,15 9,20 0,15 0,5" fill="var(--ink)"/><path d="M5 8h2l5-3v10l-5-3H5z" fill="var(--white)"/></svg>
    <h4 class="step-title">Creative Marketing</h4>
    <p class="step-text">Euismod tincidunt utthis laoreet<br>dolore magna aliquam</p>
  </div>
  <div class="step" style="left:396px;top:260px">
    <svg class="step-icon" viewBox="0 0 18 20" aria-hidden="true"><polygon points="9,0 18,5 18,15 9,20 0,15 0,5" fill="var(--ink)"/><path d="M5 8h2l5-3v10l-5-3H5z" fill="var(--white)"/></svg>
    <h4 class="step-title">Creative Marketing</h4>
    <p class="step-text">Euismod tincidunt utthis laoreet<br>dolore magna aliquam</p>
  </div>
  <div class="step" style="left:556px;top:134px">
    <svg class="step-icon" viewBox="0 0 18 20" aria-hidden="true"><polygon points="9,0 18,5 18,15 9,20 0,15 0,5" fill="var(--ink)"/><circle cx="9" cy="9" r="3.5" fill="none" stroke="var(--white)" stroke-width="1.2"/><rect x="7.5" y="12.5" width="3" height="2" fill="var(--white)"/></svg>
    <h4 class="step-title">Creative Technology</h4>
    <p class="step-text">Euismod tincidunt utthis laoreet<br>dolore magna aliquam erat</p>
  </div>
  <div class="step" style="left:556px;top:197px">
    <svg class="step-icon" viewBox="0 0 18 20" aria-hidden="true"><polygon points="9,0 18,5 18,15 9,20 0,15 0,5" fill="var(--ink)"/><circle cx="9" cy="9" r="3.5" fill="none" stroke="var(--white)" stroke-width="1.2"/><rect x="7.5" y="12.5" width="3" height="2" fill="var(--white)"/></svg>
    <h4 class="step-title">Creative Technology</h4>
    <p class="step-text">Euismod tincidunt utthis laoreet<br>dolore magna aliquam erat</p>
  </div>
  <div class="step" style="left:556px;top:260px">
    <svg class="step-icon" viewBox="0 0 18 20" aria-hidden="true"><polygon points="9,0 18,5 18,15 9,20 0,15 0,5" fill="var(--ink)"/><circle cx="9" cy="9" r="3.5" fill="none" stroke="var(--white)" stroke-width="1.2"/><rect x="7.5" y="12.5" width="3" height="2" fill="var(--white)"/></svg>
    <h4 class="step-title">Creative Technology</h4>
    <p class="step-text">Euismod tincidunt utthis laoreet<br>dolore magna aliquam erat</p>
  </div>

  <span class="name-mark" style="left:402px;top:428px;color:var(--white);font-size:10px">Northfield Renewal</span>
  <div class="rule-v rule-v--light" style="left:524px;top:403px;height:60px"></div>
  <span class="quote-mark" style="left:535px;top:373px;font-size:40px;height:26px">”</span>
  <p class="quote-text" style="left:537px;width:115px;top:400px;font-size:10.5px;line-height:1.55">Lorem ipsum dolor thesit amet, consec-tetueri that adipisc-ing elitsed .</p>

  <div class="fold"></div>
</section>

<!-- Outside spread -->
<section class="spread spread--outside" aria-label="Outside spread: back and front cover">
  <div class="photo" role="img" aria-label="Faded photo of restoration crew outside a house"
       style="background:linear-gradient(170deg,#e6e6e6 0%,#cfcfcf 45%,#e2e2e2 75%,#d4d4d4 100%)"></div>
  <div class="photo" role="img" aria-label="Photo of a technician cleaning a flooded floor in a living room"
       style="clip-path:polygon(64.6% 0,100% 0,100% 65.6%,64.6% 43.75%);background:linear-gradient(160deg,#d9d5cc 0%,#8d8a83 35%,#2f4a72 55%,#3d3a35 80%,#b7b3ab 100%)"></div>
  <svg class="shape" width="680" height="480" viewBox="0 0 680 480" aria-hidden="true">
    <polygon points="0,0 340,0 340,190 176,103 0,150" fill="var(--ink)"/>
    <polygon points="176,113 408,210 408,236 176,136" fill="var(--ink)"/>
    <polygon points="340,0 439,0 439,206 340,162" fill="var(--ink)"/>
    <polygon points="545,262 680,319 680,350 545,292" fill="var(--ink)"/>
  </svg>
  <div class="photo" role="img" aria-label="Photo of a technician inspecting a damaged wall"
       style="clip-path:polygon(0 5.8%,25.9% 20.8%,0 30.4%);background:linear-gradient(135deg,#9ea3ab 0%,#c9c2b6 50%,#5e554b 100%)"></div>

  <p class="intro-note">There are many variations of passages of Lorem Ipsum avail-able, but the majority have suf-fered alteration</p>
  <div class="rule-v rule-v--light" style="left:308px;top:23px;height:48px"></div>

  <span class="name-mark" style="left:0;width:340px;top:240px;text-align:center;font-size:20px">Northfield Renewal</span>

  <h3 class="contact-title">Contact Us</h3>
  <div class="contact-dash"></div>
  <p class="contact-line" style="left:63px;top:366px">P : +000 123 456 789<br>P : +000 123 456 789</p>
  <p class="contact-line" style="left:167px;top:366px">E : yourgmail@name.com<br>w : www.websitename.com</p>
  <p class="address">Your Street Address here, New<br>York City, Zip- 000</p>

  <span class="vertical-name">Northfield Renewal</span>

  <h1 class="cover-title"><span class="eyebrow">CORPORATE</span><span class="main">BROCHURE</span><span class="main">DESIGN.</span></h1>
  <div class="cover-underline"></div>
  <p class="cover-text">Lorem ipsum dolor sit ametconsectetuer adipiscing elit sed diam nonummy nibh euis. Lorem ipsum dolor sit ametconsectetuer adipiscing elit sed diam nonummy nibh.</p>
  <p class="cover-url">northfield-renewal.example</p>

  <div class="fold"></div>
</section>

</body>
</html>
```